Guaranteed Job - Sleek Sexy Business Card UV Spot

Im looking for a sleek and sexy business card, that resembles elite or VIP status status.
our business is corinvale.example
you can view our products on there, but our main audience for handing out our cards will be for people in the hospitality industry, so it will need to impress high management and CEO of hotels and restaurants, bars, clubs etc...
the card features will have UV spot on both sides, 400gsm stock. standard size.
Artwork should be 86 x 54mm + 2mm bleed = 90 x 58mm
it should have a nice "unique" uv spot pattern that highlights the card, not a repeated pattern, theres no originality there, and it will be disregarded.
The written material will be:
Corin Vale Hospitality College (logo)
Tobin Marsh
Director
Phone: 1300 615 737
Mobile: 0455 817 296
Email: info@corinvale.example
website: www.corinvale.example
I'm looking for originality here, i don't want just a simple stock card, want something that has a wow factor for people.
You will find the logo attached. you may invert the white to black words to suit the background as you please.
thank you and good luck
As a side note, ive received a lot of proposals, im too busy to give feedback to each and every one, so if i havent provided feedback for your design within 24 hours, then consider it not acceptable, and you could resubmit another design.
So far i have not seen any design that stood out for me, they all seem pretty generic. there nothing thats unique, i would figure for the amount that im offering, that people would put some more effort and creativity into the design.
so far over 200 designs submitted, and nothing i have seen looks very original, everything looks like a different variation of the same stuff, i said it very clearly i wanted something unique, the only thing that has come close to it so far is this one
Reason: Ive received alot of design concepts and i have reviewed everyone, but i havent had time to give feedback to every single one, only the ones that have interested me, if i havent responded, its because i havent found it good enough.
so far only a few design have been on par with what ive been looking for, an attractive eye popping design.
heres a few of them,
http://files.pixelbazaar.example/design_img/51736/62418/62418_2840915_51736_image.jpg
http://files.pixelbazaar.example/design_img/51736/68254/68254_2841377_51736_image.jpg
theyre, both unique and original, and eye catching, the only thing theyre missing is the sexyness.
if you still think you have some creativity left in your minds, then throw it on here.
Reason: Sorry guys for the delay, I was in a serious accident and out of commission for the past few months, I'm just slowly recovering now, please bare with me as i try to attend to this project, it may take me awhile as I have other projects that are on standby, I'm not 100% at the moment, so im extending the deadline for 2 weeks right now. Thanks for your patience.
Hospitality

```html
<!DOCTYPE html>
<html lang="en">
<head>
<meta charset="utf-8">
<title>Corin Vale Hospitality College – Business Card</title>
<link rel="stylesheet" href="https://fonts.googleapis.com/css2?family=Roboto+Condensed:wght@400;700&family=Roboto:wght@400;700&display=swap">
<style>
  :root {
    --page-bg: #e6e7e9;
    --card-black: #0b0b0d;
    --ink-dark: #1f252d;
    --ink-white: #ffffff;
    --band-white: #ffffff;
    --tile-sky: #9fd8f5;
    --tile-blue: #5aa9e2;
    --tile-violet: #8a4fc4;
    --tile-pink: #e8409a;
    --tile-magenta: #c81f6e;
  }
  html, body {
    margin: 0;
    width: 1200px;
    height: 861px;
    overflow: hidden;
    background: var(--page-bg);
  }
  .stage {
    position: relative;
    width: 1200px;
    height: 861px;
  }
  .card {
    position: absolute;
    top: 268px;
    width: 520px;
    height: 326px;
    border-radius: 14px;
    overflow: hidden;
    box-shadow: 0 10px 30px rgba(0,0,0,.25);
    font-family: "Roboto", Arial, sans-serif;
  }
  .card--front { left: 50px; }
  .card--back { left: 630px; }
  .card-art {
    position: absolute;
    inset: 0;
    width: 520px;
    height: 326px;
  }
  .brand {
    position: absolute;
    font-family: "Roboto Condensed", Arial, sans-serif;
    font-weight: 700;
    color: var(--ink-dark);
    line-height: 1;
    display: flex;
    align-items: center;
    gap: 10px;
  }
  .brand-mark {
    width: 34px;
    height: 34px;
    background: var(--ink-dark);
    flex: none;
  }
  .brand-name {
    font-size: 24px;
    text-transform: uppercase;
    letter-spacing: .5px;
  }
  .brand-name small {
    display: block;
    font-size: 11px;
    margin-top: 4px;
    letter-spacing: .3px;
  }
  .card--front .brand { left: 270px; top: 82px; }
  .card--back .brand { left: 318px; top: 82px; }
  .website-large {
    position: absolute;
    left: 30px;
    top: 230px;
    color: var(--ink-white);
    font-weight: 700;
    font-size: 24px;
  }
  .holder {
    position: absolute;
    left: 22px;
    top: 66px;
    color: var(--ink-dark);
    font-family: "Roboto Condensed", Arial, sans-serif;
  }
  .holder-name {
    font-weight: 700;
    font-size: 40px;
    line-height: 1;
    text-transform: uppercase;
  }
  .holder-title {
    font-size: 22px;
    line-height: 1.1;
  }
  .contact-list {
    position: absolute;
    left: 24px;
    top: 184px;
    margin: 0;
    padding: 0;
    list-style: none;
    color: var(--ink-white);
    font-size: 19px;
  }
  .contact-list li {
    display: flex;
    align-items: center;
    gap: 12px;
    height: 30px;
  }
  .contact-icon {
    width: 20px;
    height: 20px;
    flex: none;
  }
</style>
</head>
<body>
<svg width="0" height="0" style="position:absolute" aria-hidden="true">
  <defs>
    <linearGradient id="tileGlow" x1="0" y1="0" x2="1" y2="1">
      <stop offset="0" stop-color="var(--tile-sky)"/>
      <stop offset=".4" stop-color="var(--tile-blue)"/>
      <stop offset=".6" stop-color="var(--tile-violet)"/>
      <stop offset=".8" stop-color="var(--tile-pink)"/>
      <stop offset="1" stop-color="var(--tile-magenta)"/>
    </linearGradient>
    <linearGradient id="topSpectrum" x1="0" y1="0" x2="1" y2="0">
      <stop offset="0" stop-color="#3a1f4d"/>
      <stop offset=".3" stop-color="#7b4fd1"/>
      <stop offset=".5" stop-color="#47b6e8"/>
      <stop offset=".7" stop-color="#9ad64a"/>
      <stop offset=".85" stop-color="#f2d23b"/>
      <stop offset="1" stop-color="#ee7a2f"/>
    </linearGradient>
    <linearGradient id="swooshEdge" x1="0" y1="0" x2="1" y2="1">
      <stop offset="0" stop-color="#f0a9c8"/>
      <stop offset=".45" stop-color="#e8d53a"/>
      <stop offset=".75" stop-color="#5fd27a"/>
      <stop offset="1" stop-color="#35c6e0"/>
    </linearGradient>
    <linearGradient id="bandFade" x1="0" y1="0" x2="1" y2="0">
      <stop offset="0" stop-color="#fff" stop-opacity=".55"/>
      <stop offset=".5" stop-color="#fff" stop-opacity=".9"/>
      <stop offset="1" stop-color="#fff" stop-opacity=".95"/>
    </linearGradient>
  </defs>
</svg>

<main class="stage">
  <section class="card card--front">
    <svg class="card-art" viewBox="0 0 520 326">
      <rect width="520" height="326" fill="var(--card-black)"/>
      <rect width="520" height="326" fill="url(#tileGlow)" role="img" aria-label="Colourful glowing mosaic tile pattern"/>
      <path d="M0,0 H520 V40 Q300,8 0,72 Z" fill="url(#topSpectrum)"/>
      <path d="M0,72 Q300,8 520,40 V150 Q300,135 0,200 Z" fill="url(#bandFade)"/>
      <path d="M0,150 Q260,118 440,326 H0 Z" fill="var(--card-black)"/>
      <path d="M0,150 Q260,118 440,326" fill="none" stroke="url(#swooshEdge)" stroke-width="5" opacity=".85"/>
    </svg>
    <div class="brand">
      <span class="brand-mark"></span>
      <span class="brand-name">Corin Vale<small>Hospitality College</small></span>
    </div>
    <div class="website-large">www.corinvale.example</div>
  </section>

  <section class="card card--back">
    <svg class="card-art" viewBox="0 0 520 326">
      <rect width="520" height="326" fill="var(--card-black)"/>
      <rect width="520" height="326" fill="url(#tileGlow)" role="img" aria-label="Colourful glowing mosaic tile pattern"/>
      <path d="M0,0 H520 V40 Q300,8 0,72 Z" fill="url(#topSpectrum)"/>
      <path d="M0,72 Q300,8 520,40 V150 Q300,135 0,200 Z" fill="url(#bandFade)"/>
      <path d="M0,150 Q260,118 440,326 H0 Z" fill="var(--card-black)"/>
      <path d="M0,150 Q260,118 440,326" fill="none" stroke="url(#swooshEdge)" stroke-width="5" opacity=".85"/>
    </svg>
    <div class="holder">
      <div class="holder-name">Tobin Marsh</div>
      <div class="holder-title">Director</div>
    </div>
    <div class="brand">
      <span class="brand-mark"></span>
      <span class="brand-name">Corin Vale<small>Hospitality College</small></span>
    </div>
    <ul class="contact-list">
      <li>
        <svg class="contact-icon" viewBox="0 0 20 20" aria-hidden="true"><circle cx="10" cy="10" r="9" fill="none" stroke="#fff" stroke-width="1.5"/><path d="M6,7 q0,6 7,7 l1,-2 -2,-1 -1,1 q-3,-1 -4,-4 l1,-1 -1,-2 Z" fill="#fff"/></svg>
        <span>1300 615 737</span>
      </li>
      <li>
        <svg class="contact-icon" viewBox="0 0 20 20" aria-hidden="true"><circle cx="10" cy="10" r="9" fill="none" stroke="#fff" stroke-width="1.5"/><rect x="7" y="4.5" width="6" height="11" rx="1" fill="none" stroke="#fff" stroke-width="1.4"/></svg>
        <span>0455 817 296</span>
      </li>
      <li>
        <svg class="contact-icon" viewBox="0 0 20 20" aria-hidden="true"><circle cx="10" cy="10" r="9" fill="none" stroke="#fff" stroke-width="1.5"/><rect x="5" y="6.5" width="10" height="7" fill="none" stroke="#fff" stroke-width="1.3"/><path d="M5,6.5 L10,10.5 L15,6.5" fill="none" stroke="#fff" stroke-width="1.3"/></svg>
        <span>info@corinvale.example</span>
      </li>
      <li>
        <svg class="contact-icon" viewBox="0 0 20 20" aria-hidden="true"><circle cx="10" cy="10" r="9" fill="none" stroke="#fff" stroke-width="1.5"/><rect x="5" y="6" width="10" height="7" fill="none" stroke="#fff" stroke-width="1.3"/><path d="M8,15 H12" stroke="#fff" stroke-width="1.3"/></svg>
        <span>www.corinvale.example</span>
      </li>
    </ul>
  </section>
</main>
</body>
</html>
```